Re-launching marine insurance adjusting company - looking for energy

I am a sole practitioner specializing in the profession of average adjusting. There is an on-line brochure at www.kbrtmarine.example I am one of only a handful of specialists in this field and I enjoy a fair amount of name recognition, domestically in the US and internationally. My principal markets are the US, the London and Scandinavian insurance markets and shipowners and insurers in Latin America.
The business is a mixture of law, accounting and insurance and my clientele relies on a time-sensitive and accurate work-product, clearly stating an insurance company's liability for a given claim. The identity needs to project gravitas rather than flash.
Since 1998 I have traded as "The Halloway Bureau" but have also attempted to establish the name KBRTMARINE.example so that people would visit my website.
I want to implement a single identity across my stationery, business cards and website. I have come to see "The Halloway Bureau" as rather fatuous, since there is no company, it is just me. The Internet domain KBRTMARINE is long-established and I would be reluctant to change it. I have considered trading as simply Marcus T Holloway, MTH, KBRTMARINE or attempting to come up with a name that could be abbreviated to MTH, e.g. M Holloway Tessellate - but I can't find a suitable word for the second S.
Logo-wise, I have considered a stylized MTH or KBRTMARINE redolent of waves of the sea. A nautical theme embodying a cargo ship, navigational beacon or lighthouse might be appropriate but these tend to be hackneyed.
I have attached a card that I mocked up at Zib, connoting stacking up numbers, which I really like, but I think it is too cryptic for people in most insurance companies, who don't particularly think laterally or they wouldn't work in marine insurance, and the card that I use currently, which I intended to be understated, but in fact it states nothing.
I have also attached my current letterhead, to demonstrate how I really need help.
Finally, I have attached a credentials sheet, to attempt to establish how narrow and deep is the professional niche that I occupy.
What I am looking to implement is a single logo, font, them and color scheme to use across my website, letterhead and business cards.
Over to the Pencil Guild...
Ship owners and insurance companies
Accounting

```html
<!DOCTYPE html>
<html lang="en">
<head>
<meta charset="utf-8">
<title>MTH Letterhead</title>
<link href="https://fonts.googleapis.com/css2?family=Open+Sans:wght@400;600;700&family=Great+Vibes&display=swap" rel="stylesheet">
<style>
  :root {
    --backdrop: #d6d6d6;
    --paper: #ffffff;
    --brand-red: #c0312b;
    --ink: #2b2b2b;
    --ink-soft: #6a6a6a;
  }
  * { margin: 0; padding: 0; box-sizing: border-box; }
  html, body { width: 1200px; height: 1000px; overflow: hidden; }
  body {
    background: var(--backdrop);
    font-family: "Open Sans", Arial, sans-serif;
    color: var(--ink);
    position: relative;
  }

  /* Letterhead sheet */
  .letterhead {
    position: absolute;
    left: 500px; top: 40px;
    width: 650px; height: 920px;
    background: var(--paper);
    box-shadow: 0 6px 20px rgba(0,0,0,0.12);
  }
  .edge-bar {
    position: absolute;
    width: 14px;
    background: var(--brand-red);
  }
  .edge-bar--top { left: 0; top: 58px; height: 44px; }
  .edge-bar--bottom { right: 0; top: 800px; height: 52px; }

  .letterhead__brand {
    position: absolute;
    left: 40px; top: 50px;
    color: var(--brand-red);
    font-weight: 700;
    line-height: 1;
  }
  .letterhead__brand .brand-mark { font-size: 34px; letter-spacing: 2px; }
  .letterhead__brand .brand-name { font-size: 8px; margin-top: 4px; letter-spacing: 0.3px; }

  .contact {
    position: absolute;
    top: 52px;
    font-size: 8.5px;
    line-height: 1.45;
    color: var(--ink-soft);
  }
  .contact--address { left: 200px; }
  .contact--phone { left: 370px; }
  .contact--web { left: 510px; }

  .memo {
    position: absolute;
    left: 50px; top: 170px;
    font-size: 11px;
    line-height: 1.45;
    display: grid;
    grid-template-columns: 44px auto;
    font-weight: 700;
  }
  .memo dt { font-weight: 700; }
  .memo dd { font-weight: 600; }

  .letter-body {
    position: absolute;
    left: 50px; top: 300px;
    width: 540px;
    font-size: 11px;
    line-height: 1.5;
  }
  .letter-body p { margin-bottom: 14px; }

  .signoff {
    position: absolute;
    left: 450px; top: 640px;
    text-align: center;
  }
  .signoff__script {
    font-family: "Great Vibes", cursive;
    font-size: 26px;
    color: var(--ink);
  }
  .signoff__role { font-size: 8px; letter-spacing: 0.5px; margin-top: -2px; }

  /* Standalone logo lockup */
  .logo-lockup {
    position: absolute;
    left: 80px; top: 835px;
    color: var(--brand-red);
    font-weight: 700;
    line-height: 1;
  }
  .logo-lockup .brand-mark { font-size: 84px; letter-spacing: 4px; }
  .logo-lockup .brand-name { font-size: 17px; margin-top: 6px; padding-left: 24px; }
</style>
</head>
<body>
  <article class="letterhead">
    <span class="edge-bar edge-bar--top"></span>
    <span class="edge-bar edge-bar--bottom"></span>

    <header>
      <div class="letterhead__brand">
        <div class="brand-mark">MTH</div>
        <div class="brand-name">The Halloway Bureau</div>
      </div>
      <address class="contact contact--address">18 Quayside Row<br>Portland, ME 04101, USA</address>
      <div class="contact contact--phone">Tel (207) 555 0148<br>Fax (207) 555 0173</div>
      <div class="contact contact--web">www.kbrtmarine.example<br>info@kbrtmarine.example</div>
    </header>

    <dl class="memo">
      <dt>Date:</dt><dd>September 25, 2025</dd>
      <dt>From:</dt><dd>Mr. Tobias Wren<br>Financial Director<br>Accounting</dd>
      <dt>To:</dt><dd>Mr. Anders Lyle<br>CEO Business Solution</dd>
    </dl>

    <section class="letter-body">
      <p>Lorem ipsum dolor sit amet, ei eros vidit sonet eum, sed ea aliquam offendit. Reque quando labitur nec in, no solum ceteros est. Accumsan pertinacia an qui. Te vidisse recteque pro, cu per habemus officiis, eos ex malis posidonium omittantur. Lorem ipsum dolor sit amet, ei eros vidit sonet eum, sed ea aliquam offendit. Reque quando labitur nec in, no solum ceteros est. Accumsan pertinacia an qui. Te vidisse recteque pro, cu per habemus officiis, eos ex malis posidonium omittantur. Appetere principes eloquentiam vis ei, an mea alia petentium dignissim, te justo omnium duo.</p>
      <p>Movet laoreet delicatissimi cum id. Essent dissentiet cu cum, atqui augue iriure qui ea. Liber propriae ei sed. Euismod ornatus scaevola et pro.</p>
      <p>Verterem interesset disputationi vim et, laudem persecuti quo eu. Mea viderer vulputate ut. Ad scripta scaevola appetere usu, omnium forensibus sed cu, dolorum admodum postulant mea et. Eos ut ubique graeco insolens, etiam electram assentior cum at.</p>
      <p>In eos solum verterem facilisis, magna scaevola explicari has ex, at vidisse percipitur cum. At dicam postea luptatum sea, sed te timeam principes disputando, postea scaevola eloquentiam quo eu. Cetero concludaturque cu ius, nam erat detraxit ut, in his cetero vocent erroribus. Eu sint nulla comprehensam qui. Dolor dolorum splendide ei est, id usu inani liber deterruisset.</p>
    </section>

    <div class="signoff">
      <div class="signoff__script">Signature</div>
      <div class="signoff__role">NAME / C.E.O</div>
    </div>
  </article>

  <div class="logo-lockup">
    <div class="brand-mark">MTH</div>
    <div class="brand-name">The Halloway Bureau</div>
  </div>
</body>
</html>
```